Willow Fen Beauty Co.- Label template for Australian Small Batch Skincare company

Willow Fen is a small batch, locally made, hand crafted beauty company which makes natural, ethically sourced beauty products for socially conscious consumers.
I need someone to design a product label template that have certain fields empty for example; ingredients, instructions, batch # and product name. I want to be able to fill these fields in later because I make a lot of products, and need flexibility. I want this as a template so I can fill in these fields before sending to printer.
I need two different label sizes;
-60ml amber jar. Internal Dimensions 5.5cm including lid x 50mm round diameter.
-30ml amber jar. Internal dimensions 5cm including lid x 40mm round diameter
Colour of Label: Either rose gold or white font. Depending on what looks the best. On Black background.
Target Market(s)
I am a professional working woman, wife and mother. I use products that are work for me and contain pure ingredients. I try to live a healthy lifestyle and I like products that support this.Financially secure women. Professionals. Might have own business. Majority are full time workers. $80k plus. Urban dwellers. Clean living supporters. Use organics. Have healthy diets. Mothers whose children are 10 years +.
Industry/Entity Type
Skin Care Product
Font styles to use
Other font styles liked:
- Typo (typewriter look font)
Requirements
Must have
- product label template that have certain fields empty for example; ingredients, instructions, batch # and product name. I want to be able to fill these fields in later because I make a lot of products, and need flexibility. I want this as a template so I can fill in these fields before sending to printer.
- Logo
- Ingredients- Blank field
- Space for Product name- Blank field
- Space for Product description – Blank field
- Space for Instructions- Blank field.
- Batch number (and a blank field for filling out later)
- 60 or 30 ml
- Tagline – nurturing kind hearts, fierce minds, & brave spirits
- Hand crafted with love in Melbourne
- Website- www.willowfenbeautycompany.com
- Black background, Rose gold font. Typo font. (Font that looks like typewriter)
Nice to have
- Art Deco design elements. Rose gold on black background. I want this label to represent my artisan approach to skin care formulation and production. Everything is handmade by me.
Should not have
- Mass production feel

```html
<!DOCTYPE html>
<html lang="en">
<head>
<meta charset="utf-8">
<title>Willow Fen Beauty Co. – Jar Label Template</title>
<link href="https://fonts.googleapis.com/css2?family=Kreon:wght@300;400&family=Oswald:wght@500&display=swap" rel="stylesheet">
<style>
  :root {
    --paper: #ffffff;
    --label-black: #000000;
    --ink-white: #ffffff;
    --rose: #ef8b8f;
    --rose-light: #f6c3b4;
    --rose-gold: #c8967a;
    --bronze: #8a5a3c;
  }
  * { margin: 0; padding: 0; box-sizing: border-box; }
  html, body {
    width: 1200px; height: 800px; overflow: hidden;
    background: var(--paper);
  }
  .canvas { position: relative; width: 1200px; height: 800px; }

  .label {
    position: absolute; left: 49px; top: 125px;
    width: 1095px; height: 541px;
    background: var(--label-black);
    font-family: "Kreon", Georgia, serif;
    color: var(--ink-white);
  }

  .label__pattern {
    position: absolute; left: 73px; top: 0;
    width: 956px; height: 541px;
    background:
      linear-gradient(90deg,
        rgba(239,139,143,0.38) 0%,
        rgba(246,195,180,0.28) 40%,
        rgba(255,255,255,0.26) 75%,
        rgba(255,255,255,0.30) 100%);
  }

  .label__panel {
    position: absolute; left: 275px; top: 51px;
    width: 556px; height: 394px;
    background: var(--label-black);
  }
  .label__frame { position: absolute; inset: 0; }

  .brand-name {
    position: absolute; left: 0; right: 0; top: 82px;
    text-align: center;
    font-size: 34px; font-weight: 400;
    letter-spacing: 1px;
    color: var(--rose-gold);
  }

  .field { position: absolute; left: 0; right: 0; text-align: center; font-weight: 300; }
  .field--ingredients { top: 165px; font-size: 14.5px; }
  .field--product-name { top: 191px; font-size: 29px; letter-spacing: 0.5px; }
  .field--details { top: 240px; left: 60px; right: 60px; font-size: 17.5px; line-height: 20px; }

  .side-text {
    position: absolute;
    font-size: 13.5px; font-weight: 300; line-height: 20px;
    writing-mode: vertical-rl;
    white-space: nowrap;
  }
  .side-text--origin { left: 24px; top: 145px; }
  .side-text--tagline { left: 1051px; top: 102px; transform: rotate(180deg); }

  .tag-box {
    position: absolute;
    background: var(--label-black);
    border: 2px solid var(--rose-gold);
    border-image: linear-gradient(135deg, var(--bronze), var(--rose-light), var(--rose-gold), var(--bronze)) 1;
    font-family: "Oswald", "Arial Narrow", sans-serif;
    font-weight: 500; color: var(--ink-white);
    display: flex; align-items: center;
  }
  .tag-box--batch { left: 131px; top: 473px; width: 132px; height: 48px; padding-left: 9px; font-size: 21px; }
  .tag-box--volume { left: 507px; top: 483px; width: 84px; height: 40px; justify-content: center; font-size: 20px; }
</style>
</head>
<body>
<div class="canvas">
  <section class="label">
    <div class="label__pattern" role="img" aria-label="Art deco scallop pattern in rose gold fading to white on black"></div>

    <p class="side-text side-text--origin">Hand crafted with love in Melbourne<br>www.willowfenbeautycompany.com</p>
    <p class="side-text side-text--tagline">Nurturing kind hearts, fierce minds &amp; brave spirits.</p>

    <div class="label__panel">
      <svg class="label__frame" width="556" height="394" viewBox="0 0 556 394" aria-hidden="true">
        <defs>
          <linearGradient id="frameGradient" x1="0" y1="0" x2="0" y2="1">
            <stop offset="0" stop-color="#ef8b8f"/>
            <stop offset="0.5" stop-color="#fbe2d6"/>
            <stop offset="1" stop-color="#f6b8c0"/>
          </linearGradient>
        </defs>
        <rect x="16" y="1.5" width="524" height="391" rx="22" fill="none" stroke="url(#frameGradient)" stroke-width="3"/>
      </svg>

      <p class="brand-name">Willow Fen Beauty Co.</p>
      <p class="field field--ingredients">Ingredients Ingredients Ingredients Ingredients</p>
      <p class="field field--product-name">PRODUCT NAME</p>
      <p class="field field--details">Product description: product description roduct description<br>Instructions:&nbsp; instructions&nbsp; instructions instructions</p>
    </div>

    <div class="tag-box tag-box--batch">BATCH #</div>
    <div class="tag-box tag-box--volume">60 ml</div>
  </section>
</div>
</body>
</html>
```